Velkora - 13 different skin care oil bottle label designs

We need label designs for our private label Velkora.
The labels should be designed in Adobe Illustator. Please use warm or lightening colours. We like colours. But they should have a uniform look. It is necessary to show the fruit/trees/nuts. On the back label we will have description text in four languages, a barcode, Made in France, an adress.
We will use oval clear/transparent bottles. The label size for 150 ml is 50 x 90 mm. Label size for 250 ml bottles is 60 x 115 mm.
Argan Oil 150 ml 100% PURE
Avocado Oil 150 ml 100% PURE
Castor Oil 150 ml 100% PURE
Jojoba's Oil 150 ml 100% PURE
Apricot Oil 150 ml 100% PURE
Coconut Oil 150 ml 100% PURE
Macadamia's Oil 150 ml 100% PURE
Neem Oil 150 ml 100% PURE
Almond Oil 150 ml 100% PURE
Wheat germ Oil 150 ml 100% PURE
Pure Glycerine 250 ml
Pure Glycerine + rose water 250 ml
Parafin Oil 250 ml

```html
<!DOCTYPE html>
<html lang="en">
<head>
<meta charset="utf-8">
<title>Velkora – Skin Care Oil Labels</title>
<link rel="stylesheet" href="https://fonts.googleapis.com/css2?family=Acme&family=Quicksand:wght@500;700&display=swap">
<style>
  :root {
    --paper: #ffffff;
    --brand-green: #9ccb3b;
    --white: #ffffff;

    --argan: #8a6b5c;   --argan-ink: #7b5a4c;   --argan-a: #6e4a35; --argan-b: #a88a70;
    --avocado: #a6e22e; --avocado-ink: #9bd81e; --avocado-a: #4f8a2a; --avocado-b: #8fbf4a;
    --castor: #7a1a10;  --castor-ink: #7a1b12;  --castor-a: #3a1e1a; --castor-b: #8a6a5e;
    --jojoba: #e8674a;  --jojoba-ink: #e05a3e;  --jojoba-a: #7a4a55; --jojoba-b: #b68a93;
    --apricot: #e8431c; --apricot-ink: #e23a14; --apricot-a: #e8701e; --apricot-b: #f6a86a;
    --coconut: #5a2812; --coconut-ink: #4e2010; --coconut-a: #7a4a2a; --coconut-b: #e8e0d4;
  }
  * { box-sizing: border-box; margin: 0; padding: 0; }
  html, body { width: 1140px; height: 1200px; overflow: hidden; background: var(--paper); }
  .sheet { position: relative; width: 1140px; height: 1200px; }

  .label {
    position: absolute;
    width: 312px; height: 562px;
    border-radius: 50%;
    border: 4px solid var(--tone);
    overflow: hidden;
    background: var(--white);
  }
  .label--argan   { left: 37px;  top: 4px;   --tone: var(--argan);   --ink: var(--argan-ink); }
  .label--avocado { left: 420px; top: 4px;   --tone: var(--avocado); --ink: var(--avocado-ink); }
  .label--castor  { left: 778px; top: 4px;   --tone: var(--castor);  --ink: var(--castor-ink); }
  .label--jojoba  { left: 37px;  top: 610px; --tone: var(--jojoba);  --ink: var(--jojoba-ink); }
  .label--apricot { left: 420px; top: 610px; --tone: var(--apricot); --ink: var(--apricot-ink); }
  .label--coconut { left: 778px; top: 610px; --tone: var(--coconut); --ink: var(--coconut-ink); }

  .label__art { position: absolute; left: -4px; top: -4px; width: 312px; height: 562px; }

  .brand {
    position: absolute; left: 0; right: 0; top: 38px;
    display: flex; flex-direction: column; align-items: center; gap: 6px;
  }
  .brand__dot { width: 38px; height: 38px; border-radius: 50%; background: var(--brand-green); }
  .brand__name {
    font-family: "Quicksand", sans-serif; font-weight: 500;
    font-size: 17px; letter-spacing: 0.5px; color: var(--brand-green); line-height: 1;
  }

  .label__title {
    position: absolute; left: 0; right: 0; top: 180px;
    text-align: center;
    font-family: "Acme", sans-serif;
    font-size: 44px; line-height: 42px;
    color: var(--ink);
  }
  .label--avocado .label__title { top: 162px; }

  .badge {
    position: absolute; left: 50%; top: 268px;
    width: 62px; height: 62px; margin-left: -31px;
    border-radius: 50%;
    background: var(--tone);
    border: 3px solid var(--white);
    box-shadow: 0 0 0 2px var(--tone);
    display: flex; align-items: flex-end; justify-content: center;
    padding-bottom: 8px;
  }
  .badge__drop {
    position: absolute; left: 50%; top: 10px; width: 18px; height: 18px; margin-left: -9px;
    border: 2px solid var(--white); border-radius: 0 50% 50% 50%; transform: rotate(45deg);
  }
  .badge__text {
    font-family: "Quicksand", sans-serif; font-weight: 700;
    font-size: 8px; color: var(--white); line-height: 1;
  }

  .label__volume {
    position: absolute; left: 0; right: 0; top: 490px;
    text-align: center;
    font-family: "Quicksand", sans-serif; font-weight: 700;
    font-size: 21px; color: var(--white);
  }
</style>
</head>
<body>
<main class="sheet">

  <article class="label label--argan">
    <svg class="label__art" viewBox="0 0 312 562">
      <defs><linearGradient id="g-argan" x1="0" y1="0" x2="1" y2="1"><stop offset="0" stop-color="var(--argan-a)"/><stop offset="1" stop-color="var(--argan-b)"/></linearGradient></defs>
      <path role="img" aria-label="Photo of argan nuts" d="M0 290 Q156 312 312 290 L312 562 L0 562 Z" fill="url(#g-argan)"/>
      <path d="M0 286 Q156 308 312 286" fill="none" stroke="var(--argan)" stroke-width="10"/>
    </svg>
    <div class="brand"><span class="brand__dot"></span><span class="brand__name">velkora</span></div>
    <h2 class="label__title">Argan Oil</h2>
    <div class="badge"><span class="badge__drop"></span><span class="badge__text">100% Pure</span></div>
    <p class="label__volume">150ml</p>
  </article>

  <article class="label label--avocado">
    <svg class="label__art" viewBox="0 0 312 562">
      <defs><linearGradient id="g-avocado" x1="0" y1="0" x2="1" y2="1"><stop offset="0" stop-color="var(--avocado-a)"/><stop offset="1" stop-color="var(--avocado-b)"/></linearGradient></defs>
      <path role="img" aria-label="Photo of whole avocados" d="M0 290 Q156 312 312 290 L312 562 L0 562 Z" fill="url(#g-avocado)"/>
      <path d="M0 286 Q156 308 312 286" fill="none" stroke="var(--avocado)" stroke-width="10"/>
    </svg>
    <div class="brand"><span class="brand__dot"></span><span class="brand__name">velkora</span></div>
    <h2 class="label__title">Avocado<br>Oil</h2>
    <div class="badge"><span class="badge__drop"></span><span class="badge__text">100% Pure</span></div>
    <p class="label__volume">150ml</p>
  </article>

  <article class="label label--castor">
    <svg class="label__art" viewBox="0 0 312 562">
      <defs><linearGradient id="g-castor" x1="0" y1="0" x2="1" y2="1"><stop offset="0" stop-color="var(--castor-a)"/><stop offset="1" stop-color="var(--castor-b)"/></linearGradient></defs>
      <path role="img" aria-label="Photo of speckled castor beans" d="M0 290 Q156 312 312 290 L312 562 L0 562 Z" fill="url(#g-castor)"/>
      <path d="M0 286 Q156 308 312 286" fill="none" stroke="var(--castor)" stroke-width="10"/>
    </svg>
    <div class="brand"><span class="brand__dot"></span><span class="brand__name">velkora</span></div>
    <h2 class="label__title">Castor Oil</h2>
    <div class="badge"><span class="badge__drop"></span><span class="badge__text">100% Pure</span></div>
    <p class="label__volume">150ml</p>
  </article>

  <article class="label label--jojoba">
    <svg class="label__art" viewBox="0 0 312 562">
      <defs><linearGradient id="g-jojoba" x1="0" y1="0" x2="1" y2="1"><stop offset="0" stop-color="var(--jojoba-a)"/><stop offset="1" stop-color="var(--jojoba-b)"/></linearGradient></defs>
      <path role="img" aria-label="Photo of jojoba seeds" d="M0 290 Q156 312 312 290 L312 562 L0 562 Z" fill="url(#g-jojoba)"/>
      <path d="M0 286 Q156 308 312 286" fill="none" stroke="var(--jojoba)" stroke-width="10"/>
    </svg>
    <div class="brand"><span class="brand__dot"></span><span class="brand__name">velkora</span></div>
    <h2 class="label__title">Jojoba's Oil</h2>
    <div class="badge"><span class="badge__drop"></span><span class="badge__text">100% Pure</span></div>
    <p class="label__volume">150ml</p>
  </article>

  <article class="label label--apricot">
    <svg class="label__art" viewBox="0 0 312 562">
      <defs><linearGradient id="g-apricot" x1="0" y1="0" x2="1" y2="1"><stop offset="0" stop-color="var(--apricot-a)"/><stop offset="1" stop-color="var(--apricot-b)"/></linearGradient></defs>
      <path role="img" aria-label="Photo of ripe apricots" d="M0 290 Q156 312 312 290 L312 562 L0 562 Z" fill="url(#g-apricot)"/>
      <path d="M0 286 Q156 308 312 286" fill="none" stroke="var(--apricot)" stroke-width="10"/>
    </svg>
    <div class="brand"><span class="brand__dot"></span><span class="brand__name">velkora</span></div>
    <h2 class="label__title">Apricot Oil</h2>
    <div class="badge"><span class="badge__drop"></span><span class="badge__text">100% Pure</span></div>
    <p class="label__volume">150ml</p>
  </article>

  <article class="label label--coconut">
    <svg class="label__art" viewBox="0 0 312 562">
      <defs><linearGradient id="g-coconut" x1="0" y1="0" x2="1" y2="1"><stop offset="0" stop-color="var(--coconut-a)"/><stop offset="1" stop-color="var(--coconut-b)"/></linearGradient></defs>
      <path role="img" aria-label="Photo of halved coconuts" d="M0 290 Q156 312 312 290 L312 562 L0 562 Z" fill="url(#g-coconut)"/>
      <path d="M0 286 Q156 308 312 286" fill="none" stroke="var(--coconut)" stroke-width="10"/>
    </svg>
    <div class="brand"><span class="brand__dot"></span><span class="brand__name">velkora</span></div>
    <h2 class="label__title">Coconut Oil</h2>
    <div class="badge"><span class="badge__drop"></span><span class="badge__text">100% Pure</span></div>
    <p class="label__volume">150ml</p>
  </article>

</main>
</body>
</html>
```